Lumara Health & Wellness Business Card Design

We would like to create business cards matching with our new logo design. The card should be professional looking but still have a playful side and something that would be eye catching. We are planing to open a luxury medical spa and looking to create a design based on this new logo. We are looking for a design that shows off luxury but not be gold in color. Also, while we are a more female oriented medical center we do have men that come in for our services and it should be be too feminine.

Target Market(s)

Health & Wellness. Medical patients. Luxury spa

Industry/Entity Type

Health And Wellness

Contact Information for Business Card

It should have the logo design in the front of card and back of card should have our contact information. Our current colors are peach/ coral, teal, and gray. We are looking for a modern looking design.

Font styles to use
Script

Colors
32a6d6
e667a6
86cfc6
fece3e

Requirements
Must have
• It should have our logo design. We would prefer to have a more modern look to the card.
Nice to have
• Eye-Catching Design on the personable side but still classy.
Should not have
• At this point we are looking for the best design. It should not have color purple.

```html
<!DOCTYPE html>
<html lang="en">
<head>
<meta charset="utf-8">
<title>Lumara Health &amp; Wellness – Business Card</title>
<link href="https://fonts.googleapis.com/css2?family=Open+Sans:wght@400;600;700&family=Pinyon+Script&display=swap" rel="stylesheet">
<style>
  :root {
    --backdrop: #737478;
    --paper: #e6e7e9;
    --ink: #2a2a2a;
    --teal: #008f80;
    --coral: #ff766b;
    --light-ink: #ecebe6;
  }
  * { margin: 0; padding: 0; box-sizing: border-box; }
  html, body { width: 1200px; height: 1200px; overflow: hidden; }
  body {
    background: var(--backdrop);
    font-family: "Open Sans", Arial, sans-serif;
    position: relative;
  }
  .card {
    position: absolute;
    left: 186px;
    width: 828px;
    height: 473px;
    border-radius: 32px;
    background: var(--paper);
    overflow: hidden;
  }
  .card-front { top: 63px; }
  .card-back { top: 663px; }

  /* front */
  .brand-name {
    position: absolute;
    left: 0; right: 0; top: 190px;
    text-align: center;
    font-size: 40px;
    font-weight: 600;
    color: var(--ink);
    letter-spacing: 0.5px;
  }
  .stripe-h { position: absolute; left: 0; right: 0; height: 26px; }
  .stripe-h.teal { top: 319px; background: var(--teal); }
  .stripe-h.coral { top: 362px; background: var(--coral); }
  .front-footer {
    position: absolute;
    left: 0; right: 0; top: 387px; bottom: 0;
    background: var(--ink);
    display: flex; align-items: center; justify-content: center;
  }
  .tagline {
    font-family: "Pinyon Script", cursive;
    font-size: 34px;
    color: #ffffff;
    padding-bottom: 4px;
  }

  /* back */
  .stripe-v { position: absolute; top: 0; bottom: 0; width: 26px; }
  .stripe-v.teal { left: 299px; background: var(--teal); }
  .stripe-v.coral { left: 341px; background: var(--coral); }
  .back-panel {
    position: absolute;
    left: 367px; right: 0; top: 0; bottom: 0;
    background: var(--ink);
  }
  .name-band {
    position: absolute;
    left: 0; right: 0; top: 65px; height: 115px;
    background: var(--paper);
    text-align: right;
    padding-right: 74px;
  }
  .person-name {
    margin-top: 22px;
    font-size: 38px;
    font-weight: 400;
    color: var(--ink);
    line-height: 1.1;
  }
  .person-name strong { font-weight: 700; }
  .person-role {
    font-size: 24px;
    color: var(--teal);
    line-height: 1.3;
  }
  .back-brand {
    position: absolute;
    left: 0; right: 0; top: 290px;
    text-align: center;
    font-size: 30px;
    font-weight: 600;
    color: var(--light-ink);
  }
  .contact-list { list-style: none; position: absolute; left: 51px; top: 150px; }
  .contact-item {
    position: absolute;
    left: 0;
    display: flex; align-items: center;
    width: 240px;
    font-size: 10.5px;
    font-weight: 600;
    color: var(--ink);
    line-height: 1.4;
    white-space: nowrap;
  }
  .contact-icon {
    flex: none;
    width: 38px; height: 38px;
    border-radius: 50%;
    margin-right: 13px;
    display: flex; align-items: center; justify-content: center;
  }
  .contact-icon.coral { background: var(--coral); }
  .contact-icon.teal { background: var(--teal); }
  .contact-icon svg { width: 22px; height: 22px; }
</style>
</head>
<body>

<section class="card card-front">
  <div class="brand-name">Lumara Health &amp; Wellness</div>
  <div class="stripe-h teal"></div>
  <div class="stripe-h coral"></div>
  <div class="front-footer">
    <p class="tagline">Health, Wellness And Beauty</p>
  </div>
</section>

<section class="card card-back">
  <ul class="contact-list">
    <li class="contact-item" style="top:2px">
      <span class="contact-icon coral">
        <svg viewBox="0 0 24 24" fill="#fff"><path d="M12 3 2 12h3v8h5v-5h4v5h5v-8h3z"/></svg>
      </span>
      <span>CITY ADDRESS, STREET<br>HOME LOCATION GOES HERE</span>
    </li>
    <li class="contact-item" style="top:58px">
      <span class="contact-icon teal">
        <svg viewBox="0 0 24 24" fill="none" stroke="#fff" stroke-width="2" stroke-linejoin="round"><rect x="3" y="6" width="18" height="12" rx="1"/><path d="m3 7 9 7 9-7"/></svg>
      </span>
      <span>HELLO@LUMARAHEALTH.COM</span>
    </li>
    <li class="contact-item" style="top:114px">
      <span class="contact-icon coral">
        <svg viewBox="0 0 24 24" fill="#fff"><path d="M6.6 10.8a15 15 0 0 0 6.6 6.6l2.2-2.2a1 1 0 0 1 1-.25 11.4 11.4 0 0 0 3.6.57 1 1 0 0 1 1 1V20a1 1 0 0 1-1 1A17 17 0 0 1 3 4a1 1 0 0 1 1-1h3.5a1 1 0 0 1 1 1c0 1.25.2 2.45.57 3.57a1 1 0 0 1-.25 1z"/></svg>
      </span>
      <span>PHONE: +1 555 204 7781<br>+1 555 309 4426</span>
    </li>
    <li class="contact-item" style="top:176px">
      <span class="contact-icon teal">
        <svg viewBox="0 0 24 24" fill="none" stroke="#fff" stroke-width="2"><circle cx="12" cy="12" r="9"/><path d="M3 12h18M12 3c3 3 3 15 0 18M12 3c-3 3-3 15 0 18"/></svg>
      </span>
      <span>WWW.LUMARAHEALTH.COM</span>
    </li>
  </ul>
  <div class="stripe-v teal"></div>
  <div class="stripe-v coral"></div>
  <div class="back-panel">
    <div class="name-band">
      <h1 class="person-name">DANIEL <strong>REYES</strong></h1>
      <p class="person-role">graphic designer</p>
    </div>
    <div class="back-brand">Lumara Health &amp; Wellness</div>
  </div>
</section>

</body>
</html>
```